Brine - Pop/Rock Album Artwork

Brine are a London based Rock/Indie band and this is our 2nd album. We require CD cover artwork.
Here is the artwork for our first album: https://www.vendrilo.co.uk/gp/product/X913QK44Z2?ie=UTF8&*Version*=1&*entries*=0
We like the following attached CD Covers and we are in the same genre music as these bands.
The Album will be called "Paper Hollow", the band name "BRINE" should be uppercase. Ideally the name "BRINE" will be designed in such a way that we can use this font on badges and as a Logo itself.
The track listing is:-
1 Unspun
2. 40 Tides
3. Rusty Gale
4. Kestrels
5. Bellows
6. Fold the Amber
7. Herons
8. Palmora
9. Out by Dusk
10. Pale Ember
11. Unfurl
This project should really just cover the front page of the artwork for a digital CD artwork to be used on Cadenzo and Wavvel.
Please do listen to our music here: https://echovault.com/brine

```html
<!DOCTYPE html>
<html lang="en">
<head>
<meta charset="utf-8">
<title>BRINE – Paper Hollow</title>
<link rel="stylesheet" href="https://fonts.googleapis.com/css2?family=Montserrat:wght@900&display=swap">
<style>
  :root {
    --teal: #6a9e92;
    --teal-bright: #3fae92;
    --teal-deep: #2e6c7c;
    --red: #e8322a;
    --purple: #3a2270;
    --yellow: #e9c256;
    --ink: #fffdf6;
    --shadow: rgba(20, 8, 28, 0.9);
  }
  html, body {
    margin: 0;
    padding: 0;
    width: 1200px;
    height: 1200px;
    overflow: hidden;
    background: var(--teal);
  }
  .cover {
    position: relative;
    width: 1200px;
    height: 1200px;
    overflow: hidden;
    font-family: "Montserrat", "Helvetica Neue", Arial, sans-serif;
  }
  .cover__pattern {
    position: absolute;
    inset: 0;
    background:
      radial-gradient(circle at 20% 12%, rgba(232, 50, 42, 0.55), transparent 28%),
      radial-gradient(circle at 85% 10%, rgba(63, 174, 146, 0.85), transparent 30%),
      radial-gradient(circle at 50% 22%, rgba(58, 34, 112, 0.55), transparent 30%),
      radial-gradient(circle at 15% 55%, rgba(233, 194, 86, 0.5), transparent 28%),
      radial-gradient(circle at 45% 55%, rgba(58, 34, 112, 0.6), transparent 26%),
      radial-gradient(circle at 80% 55%, rgba(233, 194, 86, 0.45), transparent 28%),
      radial-gradient(circle at 30% 78%, rgba(232, 50, 42, 0.5), transparent 26%),
      radial-gradient(circle at 75% 78%, rgba(58, 34, 112, 0.6), transparent 28%),
      radial-gradient(circle at 20% 95%, rgba(233, 194, 86, 0.55), transparent 26%),
      radial-gradient(circle at 90% 95%, rgba(232, 50, 42, 0.5), transparent 26%),
      linear-gradient(160deg, var(--teal) 0%, var(--teal-deep) 60%, var(--purple) 100%);
  }
  .cover__title,
  .cover__band {
    position: absolute;
    left: 0;
    right: 0;
    margin: 0;
    text-align: center;
    white-space: nowrap;
    color: var(--ink);
    font-weight: 900;
    line-height: 1;
    text-shadow: 6px 8px 14px var(--shadow), 0 0 22px var(--shadow);
  }
  .cover__title {
    top: 352px;
    font-size: 124px;
    letter-spacing: 0;
  }
  .cover__band {
    top: 874px;
    font-size: 172px;
    letter-spacing: 4px;
  }
</style>
</head>
<body>
  <main class="cover">
    <div class="cover__pattern" role="img" aria-label="Geometric pattern of interlocking chevrons and triangles in teal, red, purple and yellow on a worn wood texture"></div>
    <h1 class="cover__title">PAPER HOLLOW</h1>
    <h2 class="cover__band">BRINE</h2>
  </main>
</body>
</html>
```